Redesign of current website

Redesign - tmrdbllc.com

Coding

Coded - Design and coding required

Number of Pages Required

4 page

Colors

Designer to choose colors to be used in the design.

```html
<!DOCTYPE html>
<html lang="en">
<head>
<meta charset="utf-8">
<title>TMRDB, LLC — Home</title>
<link href="https://fonts.googleapis.com/css2?family=Poppins:wght@400;500;600;700&display=swap" rel="stylesheet">
<style>
:root{
  --green:#1aa51a;
  --green-dark:#128012;
  --ink:#222;
  --text:#555;
  --muted:#888;
  --line:#e3e3e3;
  --soft:#f2f2f2;
  --black:#0b0b0b;
  --white:#fff;
}
*{box-sizing:border-box;margin:0;padding:0}
html,body{width:1200px;height:3756px;overflow:hidden}
body{font-family:"Poppins",Arial,sans-serif;color:var(--ink);background:var(--white);position:relative}
a{color:inherit;text-decoration:none}
.btn{display:inline-block;background:var(--green);color:var(--white);border-radius:30px;font-size:15px;font-weight:500;padding:10px 34px}
.section-title{font-size:34px;font-weight:500;text-align:center;color:var(--ink)}

/* header */
.site-header{position:absolute;left:0;top:0;width:1200px;height:120px;background:var(--white)}
.brand{position:absolute;left:48px;top:36px;font-size:40px;font-weight:700;color:var(--green);letter-spacing:1px;display:flex;align-items:center;gap:10px}
.brand-square{width:16px;height:16px;background:var(--green)}
.topbar{position:absolute;right:56px;top:22px;display:flex;align-items:center;gap:28px;font-size:14px;color:var(--text)}
.topbar span{display:flex;align-items:center;gap:8px}
.topbar .login{background:var(--green);color:#fff;border-radius:4px;padding:4px 26px}
.main-nav{position:absolute;right:56px;top:70px;display:flex;gap:46px;font-size:15px;color:var(--ink)}
.main-nav .active{color:var(--green);border-bottom:2px solid var(--green);padding-bottom:4px}

/* hero */
.hero{position:absolute;left:0;top:120px;width:1200px;height:620px;background:linear-gradient(90deg,#d9d9d9 0%,#f4f4f4 45%,#e8e8e8 100%);overflow:hidden}
.hero-media{position:absolute;left:600px;top:20px;width:560px;height:460px;border-radius:40px;background:radial-gradient(ellipse at 50% 45%,#ffffff 0%,#d0d0d0 60%,#bdbdbd 100%)}
.hero-copy{position:absolute;left:140px;top:170px}
.hero-copy h1{font-size:40px;font-weight:600;line-height:1.25;color:var(--ink)}
.hero-copy h1 em{font-style:normal;color:var(--green)}
.hero-copy .btn{margin-top:22px}
.hero-swoosh{position:absolute;left:0;bottom:0}
.slider-arrow{position:absolute;width:38px;height:38px;border-radius:50%;background:#fff;border:1px solid #ccc;display:flex;align-items:center;justify-content:center}

/* about */
.about-media{position:absolute;left:40px;top:800px;width:560px;height:240px;border-radius:20px;background:linear-gradient(90deg,#cfcfcf,#f1f1f1 50%,#d4d4d4)}
.about-copy{position:absolute;left:632px;top:780px;width:500px}
.about-copy h2{font-size:27px;font-weight:500;line-height:1.35}
.about-copy p{font-size:13px;line-height:1.6;color:var(--text);margin-top:16px}
.about-copy .btn{margin-top:20px}

/* services */
.services-title{position:absolute;left:0;top:1148px;width:1200px}
.service-card{position:absolute;top:1220px;width:288px;height:264px;border:1px solid var(--line);background:#fff;text-align:center}
.service-card .media{height:120px;background:linear-gradient(135deg,#b08f6d,#6d5a48)}
.service-card .icon{width:34px;height:34px;margin:-4px auto 0;position:relative;top:-12px;background:#fff;border-radius:50%;display:flex;align-items:center;justify-content:center}
.service-card h3{font-size:16px;font-weight:600;margin-top:-8px}
.service-card p{font-size:11.5px;line-height:1.5;color:var(--text);padding:6px 26px 0}
.service-card .more{color:var(--green);font-size:16px;margin-top:6px}
.service-card.featured{background:var(--green);border-color:var(--green);top:1208px;height:288px;color:#fff}
.service-card.featured p,.service-card.featured .more{color:#fff}
.service-card.featured .icon{background:var(--green)}
.services-more{position:absolute;left:532px;top:1528px}

/* surveillance */
.surveillance{position:absolute;left:0;top:1620px;width:1200px;height:560px;background:linear-gradient(90deg,#efefef,#f8f8f8)}
.surveillance-copy{position:absolute;left:112px;top:170px;width:440px}
.surveillance-copy h2{font-size:36px;font-weight:500;line-height:1.2}
.surveillance-copy p{font-size:13px;line-height:1.6;color:var(--text);margin-top:16px}
.surveillance-copy .btn{margin-top:18px}
.surveillance-media{position:absolute;left:560px;top:70px;width:540px;height:420px;border-radius:24px;background:radial-gradient(ellipse at 55% 50%,#5c5c5c 0%,#2e2e2e 50%,#d8d8d8 100%)}

/* testimonials */
.eyebrow{position:absolute;left:0;top:2286px;width:1200px;text-align:center;font-size:13px;color:var(--muted)}
.testimonials-title{position:absolute;left:0;top:2312px;width:1200px}
.testimonial{position:absolute;top:2400px;width:312px;height:260px;background:#fff;border:1px solid var(--line);box-shadow:0 4px 14px rgba(0,0,0,.08);text-align:center}
.testimonial .badge{position:absolute;left:24px;top:-10px;width:38px;height:34px;background:var(--green);color:#fff;font-size:13px;font-weight:600;display:flex;align-items:center;justify-content:center}
.testimonial .avatar{width:64px;height:64px;border-radius:50%;background:linear-gradient(135deg,#d9c2aa,#8d7663);margin:26px auto 0}
.testimonial h4{font-size:15px;font-weight:600;margin-top:8px}
.testimonial .role{font-size:12px;color:var(--muted)}
.testimonial p{font-size:11.5px;line-height:1.5;color:var(--text);padding:8px 28px 0}
.testimonial .stars{color:#f5a623;font-size:16px;letter-spacing:2px;margin-top:6px}

/* partners */
.partners-title{position:absolute;left:0;top:2796px;width:1200px}
.partner-row{position:absolute;left:112px;top:2880px;width:976px;display:flex;justify-content:space-between;align-items:center}
.partner-badge{width:150px;height:44px;border-radius:6px;background:#e6e6e6}
.dots{position:absolute;left:576px;top:2976px;display:flex;gap:8px}
.dots i{width:8px;height:8px;border-radius:50%;background:#ccc;display:block}
.dots i.on{background:var(--green)}

/* contact */
.contact-title{position:absolute;left:112px;top:3052px;font-size:30px;font-weight:500}
.map-title{position:absolute;left:612px;top:3052px;font-size:30px;font-weight:500}
.contact-form{position:absolute;left:112px;top:3110px;width:480px}
.contact-form .row{display:flex;gap:20px}
.field{flex:1;border-bottom:1px solid var(--line);font-size:12px;color:var(--muted);padding:10px 0 14px}
.field.tall{height:90px}
.contact-form .btn{margin-top:18px;padding:8px 40px}
.map{position:absolute;left:612px;top:3110px;width:480px;height:200px;background:linear-gradient(135deg,#e9e5dc,#dfe6e8 60%,#e6e2d6)}

/* footer */
.site-footer{position:absolute;left:0;top:3360px;width:1200px;height:340px;background:var(--black);color:#ddd}
.footer-brand{position:absolute;left:112px;top:70px;font-size:42px;font-weight:700;color:var(--green);letter-spacing:1px}
.footer-col{position:absolute;top:70px}
.footer-col h5{font-size:15px;font-weight:500;color:#fff;margin-bottom:14px}
.footer-col li{list-style:none;font-size:12.5px;line-height:1.85;display:flex;align-items:center;gap:8px}
.footer-col li::before{content:"";width:5px;height:5px;background:var(--green);border-radius:50%}
.footer-col p{font-size:12.5px;line-height:1.7;display:flex;gap:8px;align-items:flex-start;margin-bottom:6px}
.newsletter{width:240px}
.newsletter input{display:block;width:200px;height:32px;border-radius:20px;border:none;background:#fff;font:12px "Poppins",sans-serif;text-align:center;margin-top:12px}
.newsletter .btn{width:200px;text-align:center;margin-top:10px;padding:7px 0;font-size:13px}
.social{position:absolute;left:912px;top:285px;display:flex;gap:10px}
.social i{width:24px;height:24px;border-radius:50%;background:#fff;display:block}
.copyright{position:absolute;left:0;top:3700px;width:1200px;height:56px;background:#fff;font-size:12px;color:var(--text);padding:20px 112px}
</style>
</head>
<body>

<header class="site-header">
  <a class="brand" href="#"><span class="brand-square"></span>TMRDB</a>
  <div class="topbar">
    <span><svg width="14" height="14" viewBox="0 0 24 24"><path fill="#1aa51a" d="M6.6 10.8a15 15 0 006.6 6.6l2.2-2.2a1 1 0 011-.25 11.4 11.4 0 003.6.57 1 1 0 011 1V20a1 1 0 01-1 1A17 17 0 013 4a1 1 0 011-1h3.5a1 1 0 011 1c0 1.25.2 2.45.57 3.57a1 1 0 01-.25 1z"/></svg>+1 (555) 014 2290</span>
    <span><svg width="14" height="14" viewBox="0 0 24 24"><path fill="#1aa51a" d="M2 5h20v14H2z"/><path d="M2 5l10 8 10-8" stroke="#fff" stroke-width="2" fill="none"/></svg>contact@tmrdbllc.com</span>
    <a class="login" href="#">Login</a>
  </div>
  <nav class="main-nav">
    <a class="active" href="#">Home</a>
    <a href="#">Company Overview</a>
    <a href="#">Who We Are</a>
    <a href="#">Partners and Clients</a>
    <a href="#">Contact Us</a>
  </nav>
</header>

<section class="hero">
  <div class="hero-media" role="img" aria-label="White CCTV security camera mounted on a wall bracket"></div>
  <div class="hero-copy">
    <h1>If it's important,<br>Protect it with <em>CCTV!</em></h1>
    <a class="btn" href="#">Read More</a>
  </div>
  <svg class="hero-swoosh" width="1200" height="120" viewBox="0 0 1200 120">
    <path d="M0 60 Q600 150 1200 20 L1200 120 L0 120 Z" fill="#1aa51a"/>
    <path d="M0 85 Q600 165 1200 50 L1200 120 L0 120 Z" fill="#fff"/>
  </svg>
  <div class="slider-arrow" style="left:46px;top:230px"><svg width="12" height="12" viewBox="0 0 12 12"><path d="M8 1L3 6l5 5" stroke="#333" stroke-width="2" fill="none"/></svg></div>
  <div class="slider-arrow" style="left:1116px;top:230px"><svg width="12" height="12" viewBox="0 0 12 12"><path d="M4 1l5 5-5 5" stroke="#333" stroke-width="2" fill="none"/></svg></div>
</section>

<div class="about-media" role="img" aria-label="Row of dome and bullet security cameras"></div>
<section class="about-copy">
  <h2>Tidemark Relay Data Bridge, LLC (TMRDB, LLC</h2>
  <p>We are a Self-certified Small Disabled Veteran Owned Business based in Brookfield, and we proudly serve clients across the region with dependable systems.</p>
  <p>We support our clients by supporting security, training and operational needs by using the experience gained through our military service in special operations and real world field work.</p>
  <a class="btn" href="#">Read More</a>
</section>

<h2 class="section-title services-title">Services And Products</h2>

<article class="service-card" style="left:112px">
  <div class="media" role="img" aria-label="Technician hands working on network cabling"></div>
  <div class="icon"><svg width="20" height="20" viewBox="0 0 24 24"><path d="M4 20l9-9M14 4l6 6-3 3-6-6z" stroke="#1aa51a" stroke-width="2" fill="none"/></svg></div>
  <h3>Technical Services</h3>
  <p>Lorem ipsum is simply dummy text of the printing and typesetting industry. Lorem Ipsum has been the industry.</p>
  <div class="more">&#8594;</div>
</article>
<article class="service-card featured" style="left:456px">
  <div class="media" role="img" aria-label="Stacked cardboard boxes in a warehouse" style="background:linear-gradient(135deg,#c9a57a,#7a6046)"></div>
  <div class="icon"><svg width="20" height="20" viewBox="0 0 24 24"><path d="M3 7h12v10H3zM15 10h4l2 3v4h-6z" stroke="#fff" stroke-width="2" fill="none"/></svg></div>
  <h3>Logistics Services</h3>
  <p>Lorem ipsum is simply dummy text of the printing and typesetting industry. Lorem Ipsum has been the industry.</p>
  <div class="more">&#8594;</div>
</article>
<article class="service-card" style="left:800px">
  <div class="media" role="img" aria-label="Monitor showing marketing graphics on a desk" style="background:linear-gradient(135deg,#9a9a9a,#505050)"></div>
  <div class="icon"><svg width="20" height="20" viewBox="0 0 24 24"><path d="M4 18V10M10 18V6M16 18v-5M22 18H2" stroke="#1aa51a" stroke-width="2" fill="none"/></svg></div>
  <h3>Product Marketing Services</h3>
  <p>Lorem ipsum is simply dummy text of the printing and typesetting industry. Lorem Ipsum has been the industry.</p>
  <div class="more">&#8594;</div>
</article>
<a class="btn services-more" href="#">View More</a>

<section class="surveillance">
  <div class="surveillance-copy">
    <h2>Surveillance Cameras<br>System</h2>
    <p>The Vantor is a revolutionary multi sensor PTZ camera providing a long range 33X visible day/night camera, long range thermal infrared vision, and full IR illumination with 1.8km range that powers the Vantor to provide high resolution imaging in virtually any environment from fog to complete darkness.</p>
    <p>Designed for accurate positioning of weapon systems, the unit fits all needs.</p>
    <a class="btn" href="#">Read More</a>
  </div>
  <div class="surveillance-media" role="img" aria-label="Long range multi sensor PTZ surveillance camera"></div>
</section>

<div class="eyebrow">Testimonials</div>
<h2 class="section-title testimonials-title">What out customers say about us</h2>
<div class="slider-arrow" style="left:40px;top:2466px"><svg width="12" height="12" viewBox="0 0 12 12"><path d="M8 1L3 6l5 5" stroke="#333" stroke-width="2" fill="none"/></svg></div>
<div class="slider-arrow" style="left:1122px;top:2466px"><svg width="12" height="12" viewBox="0 0 12 12"><path d="M4 1l5 5-5 5" stroke="#333" stroke-width="2" fill="none"/></svg></div>

<article class="testimonial" style="left:116px">
  <div class="badge">&#8220;&#8221;</div>
  <div class="avatar" role="img" aria-label="Customer portrait"></div>
  <h4>Marcus Delaney</h4><div class="role">Director</div>
  <p>Lorem ipsum is simply dummy text of the printing and typesetting industry. Lorem ipsum has been the standard.</p>
  <div class="stars">&#9733;&#9733;&#9733;&#9733;&#9733;</div>
</article>
<article class="testimonial" style="left:444px">
  <div class="badge">&#8220;&#8221;</div>
  <div class="avatar" role="img" aria-label="Customer portrait"></div>
  <h4>Owen Pritchard</h4><div class="role">Director</div>
  <p>Lorem ipsum is simply dummy text of the printing and typesetting industry. Lorem ipsum has been the standard.</p>
  <div class="stars">&#9733;&#9733;&#9733;&#9733;&#9733;</div>
</article>
<article class="testimonial" style="left:772px">
  <div class="badge">&#8220;&#8221;</div>
  <div class="avatar" role="img" aria-label="Customer portrait"></div>
  <h4>Clara Whitfield</h4><div class="role">Director</div>
  <p>Lorem ipsum is simply dummy text of the printing and typesetting industry. Lorem ipsum has been the standard.</p>
  <div class="stars">&#9733;&#9733;&#9733;&#9733;&#9733;</div>
</article>

<h2 class="section-title partners-title">Our Partners</h2>
<div class="partner-row">
  <div class="partner-badge"></div><div class="partner-badge"></div><div class="partner-badge"></div><div class="partner-badge"></div><div class="partner-badge"></div>
</div>
<div class="dots"><i class="on"></i><i></i><i></i></div>

<h2 class="contact-title">Get In Touch</h2>
<h2 class="map-title">Map</h2>
<form class="contact-form">
  <div class="row"><div class="field">Name</div><div class="field">Phone</div></div>
  <div class="row"><div class="field">Email</div></div>
  <div class="row"><div class="field tall">Message</div></div>
  <a class="btn" href="#">Send</a>
</form>
<div class="map" role="img" aria-label="Street map showing the office location"></div>

<footer class="site-footer">
  <div class="footer-brand">TMRDB</div>
  <div class="footer-col" style="left:412px">
    <h5>Quick Link</h5>
    <ul><li>Home</li><li>Company Overview</li><li>Who We Are</li><li>Partners and Clients</li><li>News</li><li>Contact Us</li></ul>
  </div>
  <div class="footer-col" style="left:632px">
    <h5>Contact Info</h5>
    <p><svg width="12" height="14" viewBox="0 0 12 16"><path d="M6 0a6 6 0 00-6 6c0 4.5 6 10 6 10s6-5.5 6-10a6 6 0 00-6-6z" fill="#1aa51a"/></svg>1200 Harbor Mill Road,<br>Brookfield, GA 30000</p>
    <p><svg width="12" height="12" viewBox="0 0 24 24"><path fill="#1aa51a" d="M6.6 10.8a15 15 0 006.6 6.6l2.2-2.2a1 1 0 011-.25 11.4 11.4 0 003.6.57 1 1 0 011 1V20a1 1 0 01-1 1A17 17 0 013 4a1 1 0 011-1h3.5a1 1 0 011 1c0 1.25.2 2.45.57 3.57a1 1 0 01-.25 1z"/></svg>+1 (555) 014 2290</p>
    <p><svg width="12" height="12" viewBox="0 0 24 24"><path fill="#1aa51a" d="M2 5h20v14H2z"/></svg>contact@tmrdbllc.com</p>
  </div>
  <div class="footer-col newsletter" style="left:872px">
    <h5>Get our Newsletter</h5>
    <p style="font-size:12px">Lorem ipsum is simply dummy text of the printing and typesetting industry.</p>
    <input type="text" value="Your Email" aria-label="Your Email">
    <a class="btn" href="#">Subscribe</a>
  </div>
  <div class="social"><i></i><i></i><i></i><i></i></div>
</footer>
<div class="copyright">Copyright &copy; 2020 Tidemark Relay. All Rights Reserved.</div>

</body>
</html>
```